Design for three pages of a 12-page 4-color 8.5 x 11 magazine-type booklet

We will be taking the information from a webpage at glowmerestudies.org and putting it into a 12-page 4-color 8.5 x 11 magazine-type booklet that will look like an upscale company report. I need to have a design in Photoshop for the cover and two inside pages that I can use as the template for the pages. I likely will also need help putting it together once I start putting the contents into the pages. I may just decide on the content and have the designer create the booklet as an additional freelance contract. First, I need a design for (1) the front cover, (2) one information page taken from information on http://www.glowmerestudies.org/kvon-project-management-staff/, and (3) one of the pages that has a researcher from this page on it: http://www.glowmerestudies.org/teaching-people-how-to-have/. That's designs for three pages. The designs have to be very professional looking and businesslike. We will be using the booklet to pitch to foundations and philanthropists. The work on the publication itself would be additional freelance work on an hourly basis.

Serif

• Professional look

```html
<!DOCTYPE html>
<html lang="en">
<head>
<meta charset="utf-8">
<title>Glowmere Studies booklet – cover and inside spread</title>
<link href="https://fonts.googleapis.com/css2?family=Oswald:wght@300;400;500&family=Source+Sans+3:wght@400;600;700&display=swap" rel="stylesheet">
<style>
:root{
  --stage:#3e4a4f;
  --paper:#ffffff;
  --blue:#2a7fc4;
  --blue-deep:#1f5f96;
  --ink:#2e3338;
  --grey:#6c7278;
  --line-light:#9fc9e6;
}
*{box-sizing:border-box;margin:0;padding:0}
html,body{width:1200px;height:768px;overflow:hidden;background:var(--stage)}
body{position:relative;font-family:"Source Sans 3",Arial,sans-serif;color:var(--ink)}
.page{position:absolute;top:144px;width:372px;height:480px;background:var(--paper);overflow:hidden}

/* Cover */
.cover{left:24px;background:linear-gradient(160deg,#2c7a92 0%,#1d5670 55%,#123a4c 100%)}
.cover-photo{position:absolute;left:0;top:0;width:100%;height:390px;
  background:radial-gradient(ellipse at 35% 45%,#8fc6d6 0%,#4b98b0 30%,rgba(29,86,112,0) 70%)}
.cover-title{position:absolute;right:30px;top:34px;width:120px;padding:10px 6px;border:2px solid #fff;
  font-family:"Oswald",sans-serif;font-weight:300;color:#fff;font-size:19px;line-height:1.2;text-align:center;letter-spacing:.5px}
.cover-band{position:absolute;left:0;bottom:0;width:100%;height:90px;display:flex}
.cover-logo{width:120px;background:#fff;display:flex;align-items:center;justify-content:center;gap:6px}
.logo-square{width:12px;height:12px;background:var(--blue-deep)}
.logo-name{font-family:"Oswald",sans-serif;font-weight:500;font-size:24px;color:var(--blue-deep);letter-spacing:1px}
.cover-org{flex:1;background:var(--blue-deep);color:#fff;padding:18px 14px 0;position:relative}
.cover-org h1{font-family:"Oswald",sans-serif;font-weight:300;font-size:15px;line-height:1.25;letter-spacing:.3px}
.cover-url{position:absolute;right:12px;bottom:10px;font-size:8px;color:#dbe9f4}

/* Shared inside */
.inside-left{left:444px;box-shadow:inset -14px 0 18px -14px rgba(0,0,0,.25)}
.inside-right{left:816px;box-shadow:inset 14px 0 18px -14px rgba(0,0,0,.25)}
.section-head{position:absolute;top:26px;left:22px;padding:4px 0 4px 12px;border-left:2px solid var(--blue);
  font-family:"Oswald",sans-serif;font-weight:400;font-size:20px;line-height:1.05;color:#4a4f55;letter-spacing:.5px}
.section-head::before{content:"";position:absolute;left:-2px;top:0;width:40px;height:2px;background:var(--blue)}
.folio{position:absolute;bottom:12px;font-size:6px;color:var(--grey);display:flex;align-items:center;gap:4px}
.folio .logo-name{font-size:8px}
.photo{background:linear-gradient(150deg,#c9b7a6,#8a7566)}

/* Meet the crew */
.director{position:absolute;left:34px;top:118px;right:22px;height:76px}
.director .photo{position:absolute;left:0;top:6px;width:54px;height:64px}
.director-body{margin-left:62px}
.role-tag{display:inline-block;background:var(--blue);color:#fff;font-size:6px;font-weight:700;padding:1px 8px;text-transform:uppercase}
.director-name{color:var(--blue);font-size:7px;font-weight:700;text-transform:uppercase;margin:2px 0}
.director p{font-size:6px;line-height:1.3;font-weight:400}
.crew{position:absolute;left:34px;right:22px;top:200px;display:flex;gap:4px}
.crew-member{flex:1;min-width:0}
.crew-member .photo{height:54px}
.crew-member .role-tag{display:block;text-align:center;padding:1px 0;margin:2px 0}
.crew-name{color:var(--blue);font-size:5.5px;font-weight:700;text-transform:uppercase}
.crew-member p{font-size:5.2px;line-height:1.3}

/* Approach */
.lead{position:absolute;left:22px;right:24px;top:118px;color:var(--blue);font-size:8px;font-weight:600;line-height:1.25}
.columns{position:absolute;left:22px;right:24px;top:146px;column-count:3;column-gap:12px;font-size:6px;line-height:1.3;color:var(--grey)}
.columns p{margin-bottom:7px}
.rail-photo{position:absolute;left:22px;top:258px;width:144px;height:128px;
  background:linear-gradient(180deg,#b8c98a 0%,#7f9a5c 40%,#6d6259 75%,#4a423c 100%)}
.deco-lines{position:absolute;left:160px;top:310px}
</style>
</head>
<body>

<section class="page cover">
  <div class="cover-photo" role="img" aria-label="Profile of a woman in glowing blue light with a luminous brain overlay"></div>
  <div class="cover-title">BRIDGING<br>HEAVEN<br>AND EARTH</div>
  <div class="cover-band">
    <div class="cover-logo"><span class="logo-square"></span><span class="logo-name">KVON</span></div>
    <div class="cover-org">
      <h1>GLOWMERE STUDIES AND EDUCATION INSTITUTE, INC.</h1>
      <span class="cover-url">www.glowmerestudies.org</span>
    </div>
  </div>
</section>

<section class="page inside-left">
  <h2 class="section-head">MEET<br>THE<br>CREW.</h2>
  <div class="director">
    <div class="photo" role="img" aria-label="Portrait of the director"></div>
    <div class="director-body">
      <span class="role-tag">Director</span>
      <div class="director-name">R. Martin Dovell, PhD</div>
      <p>Dr. Dovell is the president of KVON. His PhD is in supervision and developing educational programs. He is the co-author of a supervision handbook and a personality styles survey. Dr. Dovell has been a manager of communications at a telephone-billing service company, administrator of a graduate school distance-learning program, and owner and manager of two companies.</p>
    </div>
  </div>
  <div class="crew">
    <div class="crew-member">
      <div class="photo" role="img" aria-label="Portrait of the finance lead"></div>
      <span class="role-tag">Finance</span>
      <div class="crew-name">Lena Marsh</div>
      <p>Lena Marsh was employed for 21 years by a federal department, where she was awarded for outstanding service. She has helped develop accounting and business operations for a large regional hospital and a distribution company.</p>
    </div>
    <div class="crew-member">
      <div class="photo" role="img" aria-label="Portrait of the administration lead"></div>
      <span class="role-tag">Administration</span>
      <div class="crew-name">Karen Doyle</div>
      <p>Karen Doyle has been COO of an integrative medical centre and vice president of operations and human resources for a production company. She serves on advisory boards and the board of a local chamber of commerce.</p>
    </div>
    <div class="crew-member">
      <div class="photo" role="img" aria-label="Portrait of the media lead"></div>
      <span class="role-tag">Media</span>
      <div class="crew-name">Sylvia Crane</div>
      <p>Sylvia Crane is the founder and producer of a popular radio show and author of a book on grief, which encourages readers to ease the fear of death. She brings her experience to producing media for KVON.</p>
    </div>
    <div class="crew-member">
      <div class="photo" role="img" aria-label="Portrait of the education lead"></div>
      <span class="role-tag">Education</span>
      <div class="crew-name">Ray Bellamy</div>
      <p>Ray Bellamy is a history, civics and language arts teacher with a BA in English. He is also an emerging medium sitting with a development circle, and is examining how the phenomena may be taught.</p>
    </div>
    <div class="crew-member">
      <div class="photo" role="img" aria-label="Book covers from the publishing partner"></div>
      <span class="role-tag">Publication</span>
      <div class="crew-name">Wider Horizon Publications</div>
      <p>Wider Horizon Publications is a wholly owned publisher that specializes in books by emerging authors in consciousness studies, research and education, including titles on grief therapy and new developments.</p>
    </div>
  </div>
  <div class="folio" style="left:22px"><span>20</span><span class="logo-name">KVON</span></div>
</section>

<section class="page inside-right">
  <h2 class="section-head">OUR<br>APP<br>ROACH.</h2>
  <p class="lead">Afterlife Research, Development, and Education that Needs Your Support</p>
  <div class="columns">
    <p>Information about important afterlife research and education projects that now need funding follows. The list changes as projects receive funding. Please check the list regularly.</p>
    <p>Donors may give general donations to KVON in our effort to support those researchers, with KVON managing oversight of the projects, regularly reporting to the donor when requested, and disseminating the results. Or, KVON may link donors with specific afterlife researchers and either take a role in the successful completion of the work or allow the donor and grantee to work together without KVON involvement.</p>
    <p>If KVON is managing the project, the additional donation for KVON's expenses is normally around 8% of the project proposal amount.</p>
    <p>More detail about donor arrangements and bequests is at this link: Donations and Bequests</p>
    <p>Total funding that will fund all of the projects currently needing funding and KVON operations for 12 months is $5,207,000.</p>
  </div>
  <div class="rail-photo" role="img" aria-label="Railway track running into sunlit trees"></div>
  <svg class="deco-lines" width="70" height="14" viewBox="0 0 70 14" aria-hidden="true">
    <line x1="0" y1="2" x2="70" y2="2" stroke="var(--line-light)" stroke-width="2"/>
    <line x1="10" y1="9" x2="60" y2="9" stroke="var(--line-light)" stroke-width="2"/>
  </svg>
  <div class="folio" style="right:22px"><span class="logo-name">KVON</span><span>21</span></div>
</section>

</body>
</html>
```